creation of a business card design for a company specializing in the creation...

I would like to create a design for a professional business card on a black background and with the company's colors (I am attaching some files: including the logo in horizontal and centered format, I am also attaching a recent project design a T-shirt, this is the one I chose to give you an idea of my preferences.

we are in the process of developing a new website design, it is still in the development phase but it can be viewed at the following address: www.vendrelak.be to give you other ideas about the company
you will see for yourself the subject of my main activity: company specializing in the construction of stairs

I would like a business card that stands out from the rest with a unique design

here is the informations
Name: Florent Dubrec
Function: Manager
Address: Rue Masquelin du Pont 41
7180 Hainvelle
telephone: +32 486 219 508
email: info@rv8k.be
website: rv8k. be
social networks: Facebook, YouTube, TikTok, Instagram

Target Market(s)

customer who wants to have a beautiful staircase built

Industry/Entity Type

contruction d'escalier

Contact Information for Business Card

Adresse. Numero de telephone, site web, le texte : "Createur d'escalier", logo recto-verso, icone des reseaux sociaux

Requirements
Must have
• the mention: Stair creator
Nice to have
• an illustration of a designer staircase
Should not have
• do not distort the logo

```html
<!DOCTYPE html>
<html lang="fr">
<head>
<meta charset="utf-8">
<title>RV8K – Cartes de visite</title>
<link rel="stylesheet" href="https://fonts.googleapis.com/css2?family=Lato:wght@400;700;900&display=swap">
<style>
  :root {
    --page: #3a3c40;
    --card: #222325;
    --accent: #6c9cc4;
    --ink: #f2f2f2;
    --muted: #cfd3d7;
  }
  * { box-sizing: border-box; margin: 0; padding: 0; }
  html, body {
    width: 1200px; height: 952px; overflow: hidden;
    background: var(--page);
    font-family: "Lato", sans-serif;
  }
  .sheet {
    width: 1200px; height: 952px;
    display: flex; flex-direction: column;
    align-items: center; justify-content: center; gap: 56px;
  }
  .card {
    position: relative;
    width: 640px; height: 366px;
    background: var(--card);
    border-radius: 26px;
    overflow: hidden;
    box-shadow: 0 18px 40px rgba(0,0,0,.45);
  }
  .card__stripe { position: absolute; inset: 0; }

  /* Recto */
  .front-title {
    position: absolute; left: 0; right: 0; top: 118px;
    display: flex; flex-direction: column; align-items: center; gap: 10px;
  }
  .front-title__name {
    color: var(--accent); font-weight: 700; font-size: 48px; letter-spacing: .12em;
  }
  .front-title__tagline {
    color: var(--accent); font-weight: 700; font-size: 16px;
    letter-spacing: .1em; text-transform: uppercase;
  }

  /* Verso */
  .brand-lockup {
    position: absolute; left: 46px; top: 76px;
    display: flex; align-items: center; gap: 14px;
  }
  .brand-lockup__mark { width: 46px; height: 46px; background: var(--accent); }
  .brand-lockup__name {
    color: var(--ink); font-weight: 700; font-size: 52px; letter-spacing: .1em;
  }
  .contact {
    position: absolute; left: 340px; top: 52px; width: 280px;
    color: var(--ink);
  }
  .contact__name {
    color: var(--accent); font-weight: 900; font-size: 21px;
    letter-spacing: .04em; text-transform: uppercase;
  }
  .contact__role { font-size: 15px; color: var(--muted); margin-top: 2px; }
  .contact__rule { width: 54px; height: 1px; background: var(--muted); margin: 8px 0 14px; }
  .contact__list { list-style: none; display: flex; flex-direction: column; gap: 9px; }
  .contact__item { display: flex; align-items: flex-start; gap: 9px; font-size: 14px; line-height: 1.25; }
  .icon {
    flex: none; width: 20px; height: 20px; border-radius: 4px;
    background: var(--accent); display: flex; align-items: center; justify-content: center;
  }
  .icon svg { width: 13px; height: 13px; }
  .contact__footer { display: flex; align-items: center; gap: 18px; margin-top: 12px; }
  .socials { display: flex; gap: 6px; }
  .socials__dot { width: 18px; height: 18px; border-radius: 50%; background: var(--accent); }
</style>
</head>
<body>
<main class="sheet">

  <section class="card card--front" aria-label="Recto">
    <svg class="card__stripe" viewBox="0 0 640 366" preserveAspectRatio="none" aria-hidden="true">
      <line x1="0" y1="322" x2="300" y2="322" stroke="var(--accent)" stroke-width="6"/>
      <line x1="306" y1="330" x2="640" y2="330" stroke="var(--ink)" stroke-width="3"/>
    </svg>
    <div class="front-title">
      <p class="front-title__name">RV8K</p>
      <p class="front-title__tagline">Créateur d'escalier</p>
    </div>
  </section>

  <section class="card card--back" aria-label="Verso">
    <svg class="card__stripe" viewBox="0 0 640 366" preserveAspectRatio="none" aria-hidden="true">
      <line x1="0" y1="316" x2="290" y2="316" stroke="var(--ink)" stroke-width="3"/>
      <line x1="296" y1="324" x2="640" y2="324" stroke="var(--accent)" stroke-width="6"/>
    </svg>

    <div class="brand-lockup">
      <span class="brand-lockup__mark" aria-hidden="true"></span>
      <span class="brand-lockup__name">RV8K</span>
    </div>

    <div class="contact">
      <h1 class="contact__name">Florent Dubrec</h1>
      <p class="contact__role">Manager</p>
      <div class="contact__rule"></div>
      <ul class="contact__list">
        <li class="contact__item">
          <span class="icon"><svg viewBox="0 0 16 16"><path d="M8 1a5 5 0 0 0-5 5c0 4 5 9 5 9s5-5 5-9a5 5 0 0 0-5-5zm0 7a2 2 0 1 1 0-4 2 2 0 0 1 0 4z" fill="var(--card)"/></svg></span>
          <span>Rue Masquelin du Pont 41<br>7180 Hainvelle</span>
        </li>
        <li class="contact__item">
          <span class="icon"><svg viewBox="0 0 16 16"><path d="M4 1l3 3-2 2a9 9 0 0 0 5 5l2-2 3 3-2 3C7 15 1 9 1 3z" fill="var(--card)"/></svg></span>
          <span>+32 486 219 508</span>
        </li>
        <li class="contact__item">
          <span class="icon"><svg viewBox="0 0 16 16"><rect x="1" y="3" width="14" height="10" fill="none" stroke="var(--card)" stroke-width="1.6"/><path d="M1 3l7 6 7-6" fill="none" stroke="var(--card)" stroke-width="1.6"/></svg></span>
          <span>info@rv8k.be</span>
        </li>
      </ul>
      <div class="contact__footer">
        <div class="socials" aria-label="Réseaux sociaux">
          <span class="socials__dot"></span><span class="socials__dot"></span>
          <span class="socials__dot"></span><span class="socials__dot"></span>
        </div>
        <div class="contact__item">
          <span class="icon"><svg viewBox="0 0 16 16"><path d="M3 2l11 5-5 1-1 6z" fill="var(--card)"/></svg></span>
          <span>rv8k. be</span>
        </div>
      </div>
    </div>
  </section>

</main>
</body>
</html>
```